Financial e-service company needs a landing page

We need a landing page for a new start up Company.
We offer Electronic gift Cards.
We are using the primiraly the colours blue and white on our homepage. Our product is a new simple and serious financial payment way, so we need a landing page that gives a serious, professional and trustworthy look.
We are using normal browsers and would like the landing page to be scalable to different devices (tablet, phone).
In our topbar we have (se the uploaded files):
- The Company name = Glimtkassen.dk
- A home button = Hjem
- About Glimtkassen = Om Glimtkassen
- Contact us = kontakt os
- Redeem giftcard = indløs pengegave
- Sign me up = opret mig
- Log in botton = log på
At the center of the homepage we have different choice of giftcards solution as which the buyer can chose among.
- Print your personel giftcard (print selv)
- Electronic giftcard (elektronisk)
- Already have card (har kort)
I have attached our present logo - Glimtkassen by Kestrel Nine. There is a little story why the mother company is called Kestrel Nine instead of Money tree. It is because the company is started by three young guys.
Target Market(s)
Primiraly private individuals
Industry/Entity Type
Financial Service
Coding
Coded - Design and coding required
Number of Pages Required
1 page
Requirements
Must have
- - A top menu bar
- - a picture/drawning/figure (instead of the box - se screendump of homepage)
- - 3 different product choices - Print selv, Elektronisk and Har kort (se screendump homepage 1)
- - The prices of 3 different products (se screendump homepage 1)
Nice to have
- We have discused that maybe it would nice to have a log in box at the landing page, so it is for new users to sign up.
- We are open for other user minded suggestions

```html
<!DOCTYPE html>
<html lang="da">
<head>
<meta charset="utf-8">
<title>Glimtkassen.dk – Electronic Gift Cards</title>
<link href="https://fonts.googleapis.com/css2?family=Roboto:wght@300;400;500&display=swap" rel="stylesheet">
<style>
  :root {
    --sky: #3a9fd8;
    --sky-deep: #2e93cf;
    --navy: #0f3f86;
    --navy-dark: #0a2f6a;
    --orange: #f07a1c;
    --orange-ring: #e9e9e9;
    --ink: #222;
    --ink-soft: #444;
    --white: #fff;
    --price: #173f8a;
  }
  * { margin: 0; padding: 0; box-sizing: border-box; }
  html, body { width: 1200px; height: 1008px; overflow: hidden; }
  body {
    font-family: 'Roboto', sans-serif;
    background: var(--white);
    position: relative;
  }
  .hero-band {
    position: absolute; left: 0; top: 0; width: 1200px; height: 638px;
    background: var(--sky);
  }
  .topbar {
    position: absolute; left: 88px; top: 42px; width: 1025px; height: 72px;
    background: var(--white); border-radius: 4px;
    box-shadow: 0 14px 18px -8px rgba(0,0,0,.35);
    display: flex; align-items: center; overflow: hidden;
  }
  .brand {
    width: 219px; height: 100%; background: var(--orange);
    display: flex; align-items: center; justify-content: center;
    color: var(--white); font-weight: 500; font-size: 26px;
    text-transform: uppercase; letter-spacing: -.5px;
  }
  .nav { position: absolute; left: 0; top: 0; height: 72px; width: 100%; }
  .nav a {
    position: absolute; top: 29px; font-size: 14.5px; color: var(--ink);
    text-decoration: none; text-transform: uppercase; white-space: nowrap;
  }
  .nav .login {
    top: 17px; left: 919px; width: 88px; height: 36px; line-height: 36px;
    text-align: center; color: var(--white); font-weight: 500;
    background: linear-gradient(var(--navy), var(--navy-dark)); border-radius: 3px;
  }
  .hero-title {
    position: absolute; left: 88px; top: 240px; font-size: 43px; font-weight: 400;
    color: var(--white); letter-spacing: .3px;
  }
  .hero-text {
    position: absolute; left: 89px; top: 302px; width: 590px;
    font-size: 15px; line-height: 24px; color: var(--white); text-align: justify; font-weight: 300;
  }
  .hero-cta {
    position: absolute; left: 88px; top: 384px; width: 128px; height: 44px;
    line-height: 44px; text-align: center; color: var(--white); font-size: 16px;
    text-decoration: none; font-weight: 400;
    background: linear-gradient(var(--navy), var(--navy-dark)); border-radius: 3px;
  }
  .hero-art {
    position: absolute; left: 758px; top: 127px; width: 333px; height: 381px;
    background: radial-gradient(circle at 50% 45%, #f4d9a0 0%, #e9b663 30%, #4a5a72 60%, rgba(58,159,216,0) 75%);
    border-radius: 8px;
  }
  .products {
    position: absolute; left: 88px; top: 512px; width: 1025px; height: 342px;
    background: var(--white); border-radius: 4px;
    box-shadow: 0 0 3px rgba(0,0,0,.12);
  }
  .product {
    position: absolute; top: 0; width: 270px; text-align: center;
  }
  .product-icon {
    width: 106px; height: 106px; margin: 40px auto 0; border-radius: 50%;
    background: var(--orange); border: 4px solid var(--orange-ring);
    box-shadow: 0 2px 4px rgba(0,0,0,.2);
    display: flex; align-items: center; justify-content: center;
  }
  .product h2 {
    margin-top: 22px; font-size: 17.5px; font-weight: 400; color: var(--ink);
  }
  .product p {
    margin-top: 15px; font-size: 12.5px; line-height: 18.4px; color: var(--ink-soft); font-weight: 300;
    text-align: justify; text-align-last: center;
  }
  .product .price {
    margin-top: 22px; font-size: 17.5px; color: var(--price);
  }
  .footer {
    position: absolute; left: 0; top: 882px; width: 1200px; height: 126px;
    background: var(--sky-deep);
  }
  .copyright {
    position: absolute; left: 118px; top: 60px; font-size: 14.5px; color: var(--white); font-weight: 300;
  }
  .social { position: absolute; left: 941px; top: 50px; display: flex; gap: 9px; }
  .social span {
    width: 35px; height: 35px; border-radius: 2px; background: var(--navy);
  }
  .version {
    position: absolute; left: 1150px; top: 63px; font-size: 12px; color: var(--white);
  }
</style>
</head>
<body>
  <div class="hero-band"></div>

  <header class="topbar">
    <div class="brand">Glimtkassen.dk</div>
    <nav class="nav">
      <a href="#" style="left:295px">Hjem</a>
      <a href="#" style="left:368px">Om Glimtkassen</a>
      <a href="#" style="left:525px">Kontakt os</a>
      <a href="#" style="left:647px">Indløs pengegave</a>
      <a href="#" style="left:821px">Opret mig</a>
      <a href="#" class="login">Log på</a>
    </nav>
  </header>

  <h1 class="hero-title">ELECTRONIC GIFT CARDS</h1>
  <p class="hero-text">Lorem Ipsum has been the industry's standard dummy text ever since the 1500s, when an unknown printer took a galley of type and scrambled it to make a type specimen book. It has survived not only five centuries, but also the leap into electronic</p>
  <a href="#" class="hero-cta">CLICK HERE</a>

  <div class="hero-art" role="img" aria-label="Illustration of a hand passing a wrapped gift box out of a computer screen, with keyboard, mouse and a payment card"></div>

  <section class="products">
    <article class="product" style="left:35px">
      <div class="product-icon">
        <svg width="46" height="42" viewBox="0 0 46 42" fill="none" stroke="#fff" stroke-width="4">
          <rect x="12" y="3" width="20" height="12" fill="#fff" stroke="none"/>
          <rect x="4" y="15" width="38" height="16" rx="3" fill="#fff" stroke="none"/>
          <rect x="12" y="26" width="22" height="13" fill="#f07a1c"/>
          <circle cx="36" cy="20" r="2" fill="#f07a1c" stroke="none"/>
        </svg>
      </div>
      <h2>PRINT SELV</h2>
      <p>Lorem Ipsum has been the industry's standard dummy text ever since the 1500s, when an unknown printer took a galley of type</p>
      <div class="price">15DKK</div>
    </article>
    <article class="product" style="left:381px">
      <div class="product-icon">
        <svg width="48" height="36" viewBox="0 0 48 36">
          <rect x="0" y="0" width="48" height="36" rx="4" fill="#fff"/>
          <path d="M2 3 L24 19 L46 3" fill="none" stroke="#f07a1c" stroke-width="3.5"/>
        </svg>
      </div>
      <h2>ELEKTRONISK</h2>
      <p>Lorem Ipsum has been the industry's standard dummy text ever since the 1500s, when an unknown printer took a galley of type</p>
      <div class="price">25DKK</div>
    </article>
    <article class="product" style="left:717px;top:-6px">
      <div class="product-icon">
        <svg width="36" height="46" viewBox="0 0 36 46">
          <path d="M0 2 Q0 0 2 0 H24 L36 12 V44 Q36 46 34 46 H2 Q0 46 0 44 Z" fill="#fff"/>
          <path d="M24 0 V12 H36" fill="#f3c9a5"/>
          <rect x="8" y="22" width="20" height="3" fill="#f07a1c"/>
          <rect x="8" y="29" width="20" height="3" fill="#f07a1c"/>
          <rect x="8" y="36" width="20" height="3" fill="#f07a1c"/>
        </svg>
      </div>
      <h2>HAR KORT</h2>
      <p>Lorem Ipsum has been the industry's standard dummy text ever since the 1500s, when an unknown printer took a galley of type</p>
      <div class="price" style="margin-top:28px">10DKK</div>
    </article>
  </section>

  <footer class="footer">
    <p class="copyright">Copyright © 2016. All Rights Reserved</p>
    <div class="social" aria-label="Social links">
      <span></span><span></span><span></span><span></span>
    </div>
    <span class="version">C6</span>
  </footer>
</body>
</html>
```